Mardolin construction chemical business need advertisement

We need an advertisement as building signboard for a new company called "Mardolin"-meaning truly effective, value added building solution.
-we source the best and effective products around the world that suit the local climate conditions
- we carry varieties of quality construction chemicals products that are cost effective and suitable for any size of budget and project and even for home user DIY .
- we provide consultation and system to solve any building problems. e.g. tiling system, waterproofing system, concrete repair system, green roof system
- We provide products training and waterproofing solutions to our clients and applicators that use our products
-By utilising our products and services, will leverage the value of the properties and protect your investment.
-our mission- to provide consultancy, services to repair, to restpre and to add avlue to properties throughout the lifecycle of the building resulting in greater whole value hence not limited to develiper but to end user protecting their investment with the quality products and services we provide.
- our philosophy-"Passion towards commitment, quality, knowledge, good practice and result.
- we need the advertisement to be easily understand by End user and contractor of the service and product we provide to solve their problem
- yet also look professional to designer and architect
end user, contractor, builder, designer, achitect
Business
- -Please create a slogan, easily to understand at one glance of what type of service and products we provide.
- -less wording, the advertisement will be put at the building
- -Strong message to explain our business

```html
<!DOCTYPE html>
<html lang="en">
<head>
<meta charset="utf-8">
<title>Mardolin – Construction Chemicals</title>
<link rel="stylesheet" href="https://fonts.googleapis.com/css2?family=Bebas+Neue&display=swap">
<style>
  :root {
    --bg: #262626;
    --bg-light: #303030;
    --yellow: #f7b81b;
    --white: #ffffff;
    --figure-a: #f2a54a;
    --figure-b: #3a9fc4;
  }
  * { margin: 0; padding: 0; box-sizing: border-box; }
  html, body { width: 835px; height: 1200px; overflow: hidden; background: var(--bg); }
  .signboard {
    position: relative;
    width: 835px;
    height: 1200px;
    overflow: hidden;
    background: radial-gradient(ellipse at 70% 45%, var(--bg-light) 0%, var(--bg) 65%);
    font-family: "Bebas Neue", "Oswald", sans-serif;
  }
  .brand-name {
    position: absolute;
    z-index: 2;
    left: 28px;
    top: 22px;
    font-size: 200px;
    line-height: 1;
    color: var(--yellow);
    letter-spacing: 1px;
    font-weight: 400;
  }
  .headline {
    position: absolute;
    z-index: 2;
    left: 30px;
    top: 322px;
    font-size: 94px;
    line-height: 96px;
    color: var(--white);
    font-weight: 400;
  }
  .mascot {
    position: absolute;
    z-index: 1;
    left: 560px;
    top: 200px;
    width: 250px;
    height: 560px;
    border-radius: 40px;
    background: linear-gradient(180deg, var(--figure-a) 0%, #e9853a 55%, var(--figure-b) 100%);
    opacity: 0.9;
  }
  .benefits {
    position: absolute;
    z-index: 2;
    left: 28px;
    top: 858px;
    list-style: none;
    color: var(--yellow);
    font-size: 36px;
    line-height: 32px;
    letter-spacing: 0.2px;
  }
  .benefits li {
    position: relative;
    padding-left: 36px;
    margin-bottom: 13px;
  }
  .benefits .tick {
    position: absolute;
    left: 0;
    top: 5px;
    width: 24px;
    height: 24px;
  }
</style>
</head>
<body>
<main class="signboard">
  <h1 class="brand-name">MARDOLIN</h1>
  <h2 class="headline">WE PUT ALL<br>OUR PASSION TO<br>HELP YOU IN<br>YOUR PROJECTS</h2>
  <div class="mascot" role="img" aria-label="Cheerful cartoon construction worker in hard hat, orange vest and tool belt, gesturing toward the headline"></div>
  <ul class="benefits">
    <li><svg class="tick" viewBox="0 0 22 22"><rect x="1.5" y="3.5" width="16" height="16" rx="3" fill="none" stroke="#f7b81b" stroke-width="2.5"/><path d="M5 11l4 4 11-12" fill="none" stroke="#f7b81b" stroke-width="3" stroke-linecap="round" stroke-linejoin="round"/></svg>THE BEST AND EFFECTIVE THAT SUIT THE LOCAL CLIMATE CONDITIONS</li>
    <li><svg class="tick" viewBox="0 0 22 22"><rect x="1.5" y="3.5" width="16" height="16" rx="3" fill="none" stroke="#f7b81b" stroke-width="2.5"/><path d="M5 11l4 4 11-12" fill="none" stroke="#f7b81b" stroke-width="3" stroke-linecap="round" stroke-linejoin="round"/></svg>VARIETIES OF QUALITY CONSTRUCTION CHEMICALS PRODUCTS<br>THAT ARE COST EFFECTIVE A</li>
    <li><svg class="tick" viewBox="0 0 22 22"><rect x="1.5" y="3.5" width="16" height="16" rx="3" fill="none" stroke="#f7b81b" stroke-width="2.5"/><path d="M5 11l4 4 11-12" fill="none" stroke="#f7b81b" stroke-width="3" stroke-linecap="round" stroke-linejoin="round"/></svg>CONSULTATION AND SYSTEM TO SOLVE ANY BUILDING PROBLEMS.</li>
    <li><svg class="tick" viewBox="0 0 22 22"><rect x="1.5" y="3.5" width="16" height="16" rx="3" fill="none" stroke="#f7b81b" stroke-width="2.5"/><path d="M5 11l4 4 11-12" fill="none" stroke="#f7b81b" stroke-width="3" stroke-linecap="round" stroke-linejoin="round"/></svg>WE PROVIDE PRODUCTS TRAINING AND WATERPROOFING SOLUTIONS<br>TO OUR CLIENTS AND APPLICATORS THAT USE OUR PRODUCTS</li>
    <li><svg class="tick" viewBox="0 0 22 22"><rect x="1.5" y="3.5" width="16" height="16" rx="3" fill="none" stroke="#f7b81b" stroke-width="2.5"/><path d="M5 11l4 4 11-12" fill="none" stroke="#f7b81b" stroke-width="3" stroke-linecap="round" stroke-linejoin="round"/></svg>CONSULTANCY, SERVICES TO REPAIR, TO RESTPRE AND<br>TO ADD AVLUE TO PROPERTIES</li>
  </ul>
</main>
</body>
</html>
```